Design a Word Template and Powerpoint Template for a Venture Capital Fund

I'm looking to get a powerpoint template and word template designed ASAP under the same selected design. Its for a finance / Venture Capital business... keen to keep it clean but "pop" and stand up on its own as a strong brand, solid templates etc... Happy to talk. Thanks Kit

Target Market(s)

Venture Capital and Private Equity

Industry/Entity Type

Finance / Venture Capital / Management Consulting

Requirements
Nice to have
• Strong formatting, icons and optionality, images can be good too

```html
<!DOCTYPE html>
<html lang="en">
<head>
<meta charset="utf-8">
<title>Northvale Venture Group – Template Pages</title>
<link href="https://fonts.googleapis.com/css2?family=Open+Sans:wght@400;600&family=Roboto:wght@300;400;500&display=swap" rel="stylesheet">
<style>
  :root{
    --backdrop:#2b2b2b;
    --ink:#1c1c1e;
    --paper:#ffffff;
    --dark-page:#1d1d1f;
    --black-page:#0c0c0c;
    --grey-text:#6a6a6a;
    --light-text:#d9d9d9;
    --rule:#8a8a8a;
  }
  *{margin:0;padding:0;box-sizing:border-box}
  html,body{width:1200px;height:1128px;overflow:hidden;background:var(--backdrop)}
  body{position:relative;font-family:"Open Sans",sans-serif;color:var(--ink)}
  .page{position:absolute;width:289px;height:405px;background:var(--paper);overflow:hidden;box-shadow:0 6px 14px rgba(0,0,0,.45)}
  .abs{position:absolute}
  .brand-name{font-family:"Roboto",sans-serif;font-weight:400;letter-spacing:.12em;white-space:nowrap}
  .tiny{font-size:4.2px;line-height:5px;color:var(--grey-text)}
  .small{font-size:5px;line-height:6.8px;color:var(--grey-text)}

  /* footer shared by inner pages */
  .page-footer .footer-name{left:10px;top:385px;font-size:6px;color:var(--ink)}
  .page-footer .footer-sub{left:17px;top:392px;font-size:2.4px;letter-spacing:.3em;color:var(--ink)}
  .page-footer .footer-rule{left:62px;top:395px;width:216px;height:.6px;background:var(--rule)}

  /* cover */
  .cover{left:127px;top:128px;background:var(--dark-page)}
  .cover-photo{left:0;top:0;width:289px;height:405px;background:radial-gradient(ellipse at 40% 25%,#3a3a3d 0%,#232326 45%,#161618 100%)}
  .cover .divider{left:104px;top:62px;width:1px;height:52px;background:var(--light-text)}
  .cover .brand-name{left:112px;top:78px;font-size:13px;color:#fff}
  .cover .brand-sub{left:129px;top:94px;font-size:4.8px;letter-spacing:.35em;color:#fff}
  .cover-title{left:21px;top:206px;font-family:"Roboto",sans-serif;font-size:23px;color:#fff;letter-spacing:.05em;white-space:nowrap}
  .cover-title span{font-weight:300;color:#bdbdbd;letter-spacing:0}
  .cover-subtitle{left:21px;top:231px;font-family:"Roboto",sans-serif;font-size:12.5px;font-weight:300;color:#c9c9c9;letter-spacing:.04em}
  .cover-text{left:21px;top:260px;width:180px;color:#cfcfcf}
  .cover-text p+p{margin-top:5px}
  .cover-web{left:0;top:366px;width:289px;text-align:center;font-size:6.5px;letter-spacing:.55em;color:#fff}

  /* our service */
  .service{left:458px;top:128px}
  .heading-sm{font-family:"Roboto",sans-serif;letter-spacing:.12em;color:var(--ink)}
  .service .heading-sm{left:25px;top:87px;font-size:11.5px}
  .service-photo{left:25px;top:116px;width:170px;height:113px;background:linear-gradient(160deg,#eef1f4 0%,#c9d0d8 45%,#4a4f58 75%,#8f97a2 100%)}
  .service .about{left:25px;top:253px;font-size:7.5px}
  .service .about-text{left:25px;top:265px;width:90px}
  .service .about-text p+p{margin-top:8px}

  /* lorem ipsum */
  .vision{left:791px;top:128px}
  .vision-band{left:0;top:0;width:289px;height:146px;background:var(--dark-page)}
  .vision-title{left:0;top:50px;width:289px;text-align:center;font-family:"Open Sans",sans-serif;font-size:29px;color:#fff;letter-spacing:.06em}
  .vision-caption{left:0;top:89px;width:289px;text-align:center;font-size:7.8px;color:#bdbdbd}
  .vision-frame{left:30px;top:118px;width:229px;height:136px;background:var(--paper)}
  .vision-photo{left:37px;top:126px;width:215px;height:120px;background:linear-gradient(180deg,#d9d9d9 0%,#9a9a9a 45%,#2d2d2d 70%,#8c8c8c 100%)}
  .vision-text{left:30px;top:262px;width:229px;text-align:center}
  .vision-text p+p{margin-top:7px}

  /* business strategy */
  .strategy{left:121px;top:595px}
  .strategy-title{left:30px;top:68px;font-family:"Roboto",sans-serif;font-weight:500;font-size:14px;letter-spacing:.14em;color:var(--ink)}
  .strategy-rule{left:30px;top:91px;width:228px;height:.7px;background:var(--rule)}
  .strategy-col{top:101px;width:58px}
  .strategy-col .num{font-size:6px;color:var(--grey-text);margin-bottom:3px}
  .strategy-col p+p{margin-top:5px}
  .strategy-art{left:28px;top:205px;width:222px;height:133px;background:linear-gradient(180deg,#eef0f8 0%,#c6cbe4 60%,#dcdcdc 100%)}

  /* core competence */
  .competence{left:458px;top:595px}
  .competence .heading-sm{left:30px;top:84px;font-size:8.3px;line-height:10.5px}
  .competence-photo{left:30px;top:118px;width:151px;height:106px;background:linear-gradient(135deg,#e8e8e8 0%,#a9a9a9 50%,#5b5b5b 75%,#d0d0d0 100%)}
  .competence .core{left:34px;top:251px;font-size:10.5px;line-height:13px}
  .competence-text{left:34px;top:281px;width:92px;letter-spacing:.05em}
  .competence-text p+p{margin-top:7px}

  /* contact back page */
  .contact{left:791px;top:595px;background:var(--black-page)}
  .contact-texture{left:0;top:0;width:289px;height:405px;background:radial-gradient(ellipse at 50% 40%,#1a1a1b 0%,#0c0c0c 70%)}
  .contact .brand-name{left:0;top:159px;width:289px;text-align:center;font-size:17px;color:#fff}
  .contact .brand-sub{left:0;top:181px;width:289px;text-align:center;font-size:7px;letter-spacing:.4em;color:#fff}
  .contact-name{left:0;top:205px;width:289px;text-align:center;font-size:11.5px;color:#fff}
  .contact-line{left:0;width:289px;text-align:center;font-size:8.5px;color:#fff;display:flex;justify-content:center;align-items:center;gap:3px}
</style>
</head>
<body>

<!-- Cover -->
<section class="page cover">
  <div class="abs cover-photo" role="img" aria-label="Dark monochrome photo of a handshake over stacked coins"></div>
  <div class="abs divider"></div>
  <div class="abs brand-name">NORTHVALE</div>
  <div class="abs brand-sub brand-name">VENTURE GROUP</div>
  <h1 class="abs cover-title">BUSINESS <span>strategy</span></h1>
  <div class="abs cover-subtitle">Presentation Template</div>
  <svg class="abs" style="left:20px;top:250px" width="222" height="6">
    <line x1="2" y1="3" x2="219" y2="3" stroke="#9a9a9a" stroke-width=".7"/>
    <circle cx="2" cy="3" r="1.6" fill="#bdbdbd"/><circle cx="110" cy="3" r="1.6" fill="#bdbdbd"/><circle cx="219" cy="3" r="1.6" fill="#bdbdbd"/>
  </svg>
  <div class="abs cover-text small">
    <p>The objectives will be based on how you gain sales by acquiring and keeping customers.</p>
    <p>A marketing strategy helps convey effective messages with the right twist of marketing approaches that will maximize your sales outcome and marketing activities.</p>
  </div>
  <svg class="abs" style="left:0;top:370px" width="289" height="4">
    <line x1="0" y1="2" x2="72" y2="2" stroke="#9a9a9a" stroke-width=".7"/><circle cx="72" cy="2" r="1.3" fill="#bdbdbd"/>
    <line x1="216" y1="2" x2="289" y2="2" stroke="#9a9a9a" stroke-width=".7"/><circle cx="216" cy="2" r="1.3" fill="#bdbdbd"/>
  </svg>
  <div class="abs cover-web">www.northvale.com</div>
</section>

<!-- Our service -->
<section class="page service">
  <h2 class="abs heading-sm">OUR SERVICE</h2>
  <div class="abs service-photo" role="img" aria-label="Photo of a business team meeting around a table in a bright office"></div>
  <h3 class="abs heading-sm about">ABOUT US</h3>
  <div class="abs about-text tiny">
    <p>It is a process to allow an organization to focus resources on the greatest opportunities to increase sales and achieve the company's target.</p>
    <p>The objectives will be based on how you gain sales by acquiring and keeping customers.</p>
    <p>Lastly, improvement should be measured regularly and assessed. This is in order for you to know what is beneficial and what is not. This will help you set new targets.</p>
  </div>
  <footer class="page-footer">
    <div class="abs brand-name footer-name">NORTHVALE</div>
    <div class="abs brand-name footer-sub">VENTURE GROUP</div>
    <div class="abs footer-rule"></div>
  </footer>
</section>

<!-- Lorem ipsum -->
<section class="page vision">
  <div class="abs vision-band"></div>
  <h2 class="abs vision-title">LOREM IPSUM</h2>
  <div class="abs vision-caption">Our works is the presentation of the our vision.</div>
  <div class="abs vision-frame"></div>
  <div class="abs vision-photo" role="img" aria-label="Monochrome photo of business people silhouetted at a table against a world map"></div>
  <div class="abs vision-text small">
    <p>A marketing strategy helps convey effective messages with the right twist of marketing approaches that will maximize your sales outcome and marketing activities.</p>
    <p>The objectives will be based on how you gain sales<br>by acquiring and keeping customers.</p>
  </div>
  <footer class="page-footer">
    <div class="abs brand-name footer-name">NORTHVALE</div>
    <div class="abs brand-name footer-sub">VENTURE GROUP</div>
    <div class="abs footer-rule"></div>
  </footer>
</section>

<!-- Business strategy -->
<section class="page strategy">
  <h2 class="abs strategy-title">BUSINESS STRATEGY</h2>
  <div class="abs strategy-rule"></div>
  <div class="abs strategy-col tiny" style="left:30px">
    <div class="num">01</div>
    <p>Marketing strategy's goal is to increase sales and achieve the advantage over other competitions. It includes short term and long term activities of marketing that has to do with the analysis of a company's situation and contribute to it's objectives.</p>
  </div>
  <div class="abs strategy-col tiny" style="left:115px">
    <div class="num">02</div>
    <p>A marketing strategy helps convey effective messages with the right twist of marketing approaches that will maximize your sales outcome and marketing activities.</p>
  </div>
  <div class="abs strategy-col tiny" style="left:198px">
    <div class="num">03</div>
    <p>Strategizing the right timing that fits your customers' buying cycles will help you save money and maximize sales.</p>
    <p>The marketing plan should be innovative. It should have the details on how your sales are followed up and the activities you are doing to develop your offers.</p>
  </div>
  <div class="abs strategy-art" role="img" aria-label="Flat illustration of a team working together around an office desk with a teamwork sign"></div>
  <footer class="page-footer">
    <div class="abs brand-name footer-name">NORTHVALE</div>
    <div class="abs brand-name footer-sub">VENTURE GROUP</div>
    <div class="abs footer-rule"></div>
  </footer>
</section>

<!-- Core competence -->
<section class="page competence">
  <h2 class="abs heading-sm">OUR WORKS IS THE PRESENTATION<br>&nbsp;OF THE OUR VISION.</h2>
  <div class="abs competence-photo" role="img" aria-label="Monochrome photo of team members stacking hands together"></div>
  <h3 class="abs heading-sm core">CORE<br>COMPETENCE</h3>
  <div class="abs competence-text tiny">
    <p>A marketing strategy helps convey effective messages with the right twist of marketing approaches that will maximize your sales outcome and marketing activities.</p>
    <p>The objectives will be based on how you gain sales by acquiring and keeping customers.</p>
  </div>
  <footer class="page-footer">
    <div class="abs brand-name footer-name">NORTHVALE</div>
    <div class="abs brand-name footer-sub">VENTURE GROUP</div>
    <div class="abs footer-rule"></div>
  </footer>
</section>

<!-- Contact -->
<section class="page contact">
  <div class="abs contact-texture" role="img" aria-label="Faint network line pattern on black"></div>
  <div class="abs brand-name">NORTHVALE</div>
  <div class="abs brand-name brand-sub">VENTURE GROUP</div>
  <svg class="abs" style="left:40px;top:194px" width="208" height="6">
    <line x1="2" y1="3" x2="206" y2="3" stroke="#ffffff" stroke-width=".8"/>
    <circle cx="2" cy="3" r="1.6" fill="#fff"/><circle cx="206" cy="3" r="1.6" fill="#fff"/>
  </svg>
  <div class="abs contact-name">Kit Dalton</div>
  <div class="abs contact-line" style="top:221px">
    <svg width="7" height="7" viewBox="0 0 10 10"><circle cx="5" cy="5" r="5" fill="#fff"/><path d="M3.2 2.6c.3-.3.7-.2.9.1l.5.8c.2.3.1.6-.1.8l-.3.3c.3.6.7 1 1.3 1.3l.3-.3c.2-.2.5-.3.8-.1l.8.5c.3.2.4.6.1.9l-.4.4c-1.8.3-4.3-2.2-4-4z" fill="#000"/></svg>
    +61 400-555-019
  </div>
  <div class="abs contact-line" style="top:232px">
    <svg width="7" height="7" viewBox="0 0 10 10"><circle cx="5" cy="5" r="5" fill="#fff"/><rect x="2.3" y="3.2" width="5.4" height="3.6" fill="none" stroke="#000" stroke-width=".8"/><path d="M2.3 3.2 5 5.3 7.7 3.2" fill="none" stroke="#000" stroke-width=".8"/></svg>
    kit@kdalton.com
  </div>
</section>

</body>
</html>
```